Snooker/Billiards/CueSports Website - winner, second and 3rd paid!

We are looking to launch a website related to “cuesports”, especially snooker. Snooker is a popular sport in The UK and worldwide.

We are looking to build 2 pages with you for this contest

- the homepage
- and a page which will be used FOR EACH player we are working with and promoting (More below)

At the moment we have no idea about the design but it should be classy, ie. maybe similar to many of the high end fashion sites - maybe this kind of look?

https://www.vostrafind.co.uk/search?q=high+end+websites&espv=2&biw=1396&bih=694&source=lnms&tbm=isch&sa=X&ved=0ahUKEwiq6MaprYvPAhVoKcAKHW8mCiUQ_AUIBigB#tbm=isch&q=classy+websites

UNLESS THIS IS COMPLETELY THE WRONG IDEA FOR WHAT WE ARE DOING, we will leave it up to you to show us some of your best ideas and help us succeed!

We are more interested in the layout and design than the text at this stage. We can add gthe main text later with your help or by ourselves, but Design, look and feel is what we want to see for this contes. Obviously if you have any questions we will give you regular feedback during the time of this contest.

This will be an ecommerce site but we expect to get to the shopping cart stage in about a month

Our main marketing tool will be our website.

There are 3 core parts to our business in priority order:

1. Sales of Snooker/Billiards Equipment
We will be selling everything from the smallest items, snooker tips, chalk, to snooker cues (sticks) all the way to Major items such as snooker tables.

Here are some typical sites that sell snooker related equipment:

http://www.peterwelbeckbaizehall.com/
http://www.cuefervora.co.uk/
http://www.qrtbaize.co.uk/

2. Sale of our own branded fashion accessories: T’shirts, Caps, jackets, cologne etc etc

3. Our booking section, where we will promote famous snooker players and other sports stars for exhibitions, after dinner speaking, golf days, etc
(probably 1 page per player in the booking section with a picture, brief bio, summary of the kind of things they can be booked for and perhaps a tarrif sheet, though we may not publish this information online and prefer to ask people to contact us if they wish to book a player

Target Markets

Mainly the UK and Europe, but snooker is becoming increasingly popular in China

Demographics are mostly males aged 16 and 40

Logo Design (separate contest at a later time)

1. The design must project a sense of professionalism and have a high class feel

2. Must Have Priorities:

- Modern, professional and friendly.
- Strong emphasis on usability.
- mobile friendly - responsive

3. Should not Have:

- An anonymous cold and corporate feel.
- A too busy feel.

4. The winner of this design contest will also be awarded a freelance project to help us further develop/complete the site.

Thank You everyone and Good luck !

18-40 mainly

2 page

• - Modern, professional and friendly.
• - Strong emphasis on usability.
• - mobile friendly - responsive
• - An anonymous cold and corporate feel.
• - A too busy feel.

```html
<!DOCTYPE html>
<html lang="en">
<head>
<meta charset="utf-8">
<title>Cue Sports Home</title>
<link href="https://fonts.googleapis.com/css2?family=Arimo:ital,wght@0,400;0,700;1,700&family=Delius&family=Roboto+Condensed:wght@400;700&display=swap" rel="stylesheet">
<style>
:root{
  --header-bg:#1f1f1f;
  --nav-text:#d8d8d8;
  --brand-text:#b9b9b9;
  --hero-dark:#0a0a0a;
  --felt:#1f7a2e;
  --felt-deep:#0f4a1a;
  --gold:#c8b27a;
  --hero-title:#b8b0a2;
  --hero-copy:#b3aea6;
  --tab-line:#6b6f73;
  --tab-text:#d6d6d6;
  --shop-bg:#232425;
  --card-line:#6f7174;
  --card-text:#b8b8b8;
  --cue-placeholder:#6e6657;
  --sale-red:#d11f24;
  --cart-orange:#f7a85a;
  --paper:#d8cfc2;
  --paper-edge:#c9bfb0;
  --footer-text:#4a4744;
  --footer-soft:#8e8a84;
  --field-bg:#d9d9d9;
  --subscribe:#ea7461;
  --ball-placeholder:#1c1c1c;
}
*{box-sizing:border-box;margin:0;padding:0}
html,body{width:1200px;height:2264px;overflow:hidden;background:var(--hero-dark)}
.page{position:relative;width:1200px;height:2264px;font-family:'Arimo',sans-serif}

/* header */
.site-header{position:absolute;top:0;left:0;width:1200px;height:91px;background:linear-gradient(#2a2a2a,#181818);z-index:2}
.brand{position:absolute;left:53px;top:14px;font-family:'Arimo',sans-serif;font-weight:700;font-size:48px;line-height:60px;color:var(--brand-text);letter-spacing:-1.5px;white-space:nowrap}
.main-nav{position:absolute;top:34px;left:632px;display:flex;gap:44px}
.main-nav a{font-family:'Roboto Condensed',sans-serif;font-weight:700;font-size:21px;color:var(--nav-text);text-decoration:none;padding-bottom:7px;letter-spacing:-0.5px;white-space:nowrap}
.main-nav a.is-active{border-bottom:2px solid var(--nav-text)}

/* hero */
.hero{position:absolute;top:91px;left:0;width:1200px;height:664px;overflow:hidden}
.hero-photo{position:absolute;inset:0;background:
  linear-gradient(180deg,#0b0b0b 0%,#1a1a1a 18%,var(--felt-deep) 30%,var(--felt) 52%,#1a5f25 70%,#2a1d1a 82%,#050505 92%)}
.hero-copy{position:absolute;left:618px;top:141px;width:500px;text-align:center}
.hero-title{font-family:'Arimo',sans-serif;font-weight:700;font-size:27px;line-height:34px;color:var(--hero-title);letter-spacing:-0.4px;white-space:nowrap}
.hero-rule{height:3px;margin:6px 6px 14px;background:linear-gradient(90deg,transparent,var(--gold) 15%,var(--gold) 85%,transparent)}
.hero-text{font-size:15px;font-weight:700;line-height:25px;color:var(--hero-copy);white-space:nowrap}
.hero-button{display:inline-block;margin-top:22px;width:159px;height:47px;border:3px solid var(--gold);color:var(--hero-copy);font-size:15px;font-weight:700;line-height:41px;text-decoration:none}

/* category tabs */
.category-bar{position:absolute;top:755px;left:0;width:1200px;height:90px;background:linear-gradient(#33363a,#25282b)}
.category-bar .gap{position:absolute;top:0;height:90px;border:2px solid var(--tab-line)}
.category-tab{position:absolute;top:0;height:90px;border:2px solid var(--tab-line);background:#2e3135;display:flex;align-items:center;justify-content:center;text-align:center;font-family:'Delius',sans-serif;font-size:24px;line-height:31px;color:var(--tab-text);text-decoration:none}

/* products */
.shop{position:absolute;top:845px;left:0;width:1200px;height:800px;background:
  radial-gradient(circle at 690px 360px,#2f3031 0,#262728 260px,var(--shop-bg) 420px),
  var(--shop-bg)}
.product{position:absolute;width:346px;height:303px;border:2px solid var(--card-line);text-align:center;color:var(--card-text)}
.product .cue{position:absolute;left:39px;top:80px;width:272px;height:6px;background:var(--cue-placeholder)}
.sale-tag{position:absolute;left:68px;top:55px;height:22px;padding:0 6px 0 12px;background:var(--sale-red);color:#fff;font-weight:700;font-size:16px;line-height:22px;clip-path:polygon(8px 0,100% 0,100% 100%,8px 100%,0 50%)}
.price{position:absolute;top:104px;left:0;width:100%;font-size:18px;font-weight:700;letter-spacing:-0.5px}
.blurb{position:absolute;top:156px;left:0;width:100%;font-size:12px;font-weight:700;line-height:16px;letter-spacing:-0.3px}
.add-to-cart{position:absolute;left:109px;top:218px;width:127px;height:27px;background:var(--cart-orange);color:#2a2a2a;font-size:13px;font-weight:700;display:flex;align-items:center;justify-content:center;gap:4px;text-decoration:none}
.view-all{position:absolute;left:1025px;top:1573px;font-size:15px;font-weight:700;font-style:italic;color:#e6e6e6;text-decoration:none}

/* footer */
.site-footer{position:absolute;top:1645px;left:0;width:1200px;height:619px;background:
  radial-gradient(ellipse at 50% 40%,#ddd5c9 0,var(--paper) 55%,var(--paper-edge) 100%)}
.ball-photo{position:absolute;left:121px;top:53px;width:324px;height:324px;background:var(--ball-placeholder)}
.newsletter-lead{position:absolute;left:521px;top:78px;width:520px;text-align:center;font-family:'Delius',sans-serif;font-size:26px;line-height:34px;color:var(--footer-soft)}
.newsletter-form{position:absolute;left:521px;top:166px;width:593px;height:62px;display:flex;border:2px solid #3a3a3a;border-radius:31px;overflow:hidden}
.newsletter-field{flex:1;background:var(--field-bg);font-family:'Delius',sans-serif;font-size:26px;color:var(--footer-soft);padding-left:24px;display:flex;align-items:center}
.newsletter-submit{width:154px;background:var(--subscribe);border-left:2px solid #3a3a3a;font-family:'Delius',sans-serif;font-size:26px;color:#3a2a28;display:flex;align-items:center;justify-content:center}
.social{position:absolute;left:634px;top:317px;display:flex;gap:23px}
.social span{width:42px;height:42px;border-radius:50%;background:var(--footer-text);display:block}
.footer-links{position:absolute;left:106px;top:425px;width:980px;display:flex;justify-content:space-between}
.footer-links a{font-size:27px;color:var(--footer-text);text-decoration:none;letter-spacing:-0.3px;white-space:nowrap}
.copyright{position:absolute;left:0;top:586px;width:1200px;text-align:center;font-size:18px;font-weight:700;font-style:italic;color:var(--footer-text)}
</style>
</head>
<body>
<div class="page">

  <header class="site-header">
    <div class="brand">BRAND NAME</div>
    <nav class="main-nav">
      <a href="#" class="is-active">HOME</a>
      <a href="#">EQUIPMENT</a>
      <a href="#">OUR PRODUCTS</a>
      <a href="#">BOOKING</a>
    </nav>
  </header>

  <section class="hero">
    <div class="hero-photo" role="img" aria-label="Photo of a gloved hand placing a ball on a green snooker table with red balls in the foreground"></div>
    <div class="hero-copy">
      <h1 class="hero-title">BECOME A PRO SNOOKER PLAYER</h1>
      <div class="hero-rule"></div>
      <p class="hero-text">Lorem ipsum dolor sit amet, consectetur adipisicing<br>elit, sed do eiusmod ea commodo consequat.</p>
      <a href="#" class="hero-button">LEARN MORE</a>
    </div>
  </section>

  <nav class="category-bar">
    <span class="gap" style="left:0;width:212px"></span>
    <span class="gap" style="left:395px;width:114px"></span>
    <span class="gap" style="left:691px;width:114px"></span>
    <span class="gap" style="left:986px;width:214px"></span>
    <a href="#" class="category-tab" style="left:210px;width:187px">Snookers<br>Euquipment</a>
    <a href="#" class="category-tab" style="left:507px;width:186px">Billiards<br>Euquipment</a>
    <a href="#" class="category-tab" style="left:803px;width:185px">Clothing<br>Shop</a>
  </nav>

  <section class="shop" aria-label="Featured products"></section>

  <article class="product" style="left:51px;top:896px">
    <span class="cue" role="img" aria-label="Product photo: snooker cue"></span><span class="sale-tag">SALE</span>
    <div class="price">123.39$</div>
    <p class="blurb">Lorem ipsum dolor sit amet,<br>consectetur adipisicing elit,<br>sed do eiusmod tempor.</p>
    <a href="#" class="add-to-cart">Add to Cart <svg width="18" height="16" viewBox="0 0 18 16"><path d="M1 2h3l2 8h9l2-6H5" fill="none" stroke="#2a2a2a" stroke-width="1.6"/><circle cx="7" cy="13.5" r="1.4" fill="#2a2a2a"/><circle cx="14" cy="13.5" r="1.4" fill="#2a2a2a"/></svg></a>
  </article>
  <article class="product" style="left:427px;top:896px">
    <span class="cue" role="img" aria-label="Product photo: snooker cue"></span><span class="sale-tag">SALE</span>
    <div class="price">123.39$</div>
    <p class="blurb">Lorem ipsum dolor sit amet,<br>consectetur adipisicing elit,<br>sed do eiusmod tempor.</p>
    <a href="#" class="add-to-cart">Add to Cart <svg width="18" height="16" viewBox="0 0 18 16"><path d="M1 2h3l2 8h9l2-6H5" fill="none" stroke="#2a2a2a" stroke-width="1.6"/><circle cx="7" cy="13.5" r="1.4" fill="#2a2a2a"/><circle cx="14" cy="13.5" r="1.4" fill="#2a2a2a"/></svg></a>
  </article>
  <article class="product" style="left:804px;top:896px">
    <span class="cue" role="img" aria-label="Product photo: snooker cue"></span><span class="sale-tag">SALE</span>
    <div class="price">123.39$</div>
    <p class="blurb">Lorem ipsum dolor sit amet,<br>consectetur adipisicing elit,<br>sed do eiusmod tempor.</p>
    <a href="#" class="add-to-cart">Add to Cart <svg width="18" height="16" viewBox="0 0 18 16"><path d="M1 2h3l2 8h9l2-6H5" fill="none" stroke="#2a2a2a" stroke-width="1.6"/><circle cx="7" cy="13.5" r="1.4" fill="#2a2a2a"/><circle cx="14" cy="13.5" r="1.4" fill="#2a2a2a"/></svg></a>
  </article>
  <article class="product" style="left:51px;top:1251px">
    <span class="cue" role="img" aria-label="Product photo: snooker cue"></span><span class="sale-tag">SALE</span>
    <div class="price">123.39$</div>
    <p class="blurb">Lorem ipsum dolor sit amet,<br>consectetur adipisicing elit,<br>sed do eiusmod tempor.</p>
    <a href="#" class="add-to-cart">Add to Cart <svg width="18" height="16" viewBox="0 0 18 16"><path d="M1 2h3l2 8h9l2-6H5" fill="none" stroke="#2a2a2a" stroke-width="1.6"/><circle cx="7" cy="13.5" r="1.4" fill="#2a2a2a"/><circle cx="14" cy="13.5" r="1.4" fill="#2a2a2a"/></svg></a>
  </article>
  <article class="product" style="left:427px;top:1251px">
    <span class="cue" role="img" aria-label="Product photo: snooker cue"></span><span class="sale-tag">SALE</span>
    <div class="price">123.39$</div>
    <p class="blurb">Lorem ipsum dolor sit amet,<br>consectetur adipisicing elit,<br>sed do eiusmod tempor.</p>
    <a href="#" class="add-to-cart">Add to Cart <svg width="18" height="16" viewBox="0 0 18 16"><path d="M1 2h3l2 8h9l2-6H5" fill="none" stroke="#2a2a2a" stroke-width="1.6"/><circle cx="7" cy="13.5" r="1.4" fill="#2a2a2a"/><circle cx="14" cy="13.5" r="1.4" fill="#2a2a2a"/></svg></a>
  </article>
  <article class="product" style="left:804px;top:1251px">
    <span class="cue" role="img" aria-label="Product photo: snooker cue"></span><span class="sale-tag">SALE</span>
    <div class="price">123.39$</div>
    <p class="blurb">Lorem ipsum dolor sit amet,<br>consectetur adipisicing elit,<br>sed do eiusmod tempor.</p>
    <a href="#" class="add-to-cart">Add to Cart <svg width="18" height="16" viewBox="0 0 18 16"><path d="M1 2h3l2 8h9l2-6H5" fill="none" stroke="#2a2a2a" stroke-width="1.6"/><circle cx="7" cy="13.5" r="1.4" fill="#2a2a2a"/><circle cx="14" cy="13.5" r="1.4" fill="#2a2a2a"/></svg></a>
  </article>

  <a href="#" class="view-all">VIEW ALL&gt;&gt;</a>

  <footer class="site-footer">
    <div class="ball-photo" role="img" aria-label="Photo of a black pool ball"></div>
    <p class="newsletter-lead">Subscribe to our Newsletter<br>and keep up with our offers etc.</p>
    <div class="newsletter-form">
      <div class="newsletter-field">Enter your Email Address</div>
      <div class="newsletter-submit">Subscribe</div>
    </div>
    <div class="social" aria-label="Social links">
      <span></span><span></span><span></span><span></span><span></span>
    </div>
    <nav class="footer-links">
      <a href="#">CONTACT US</a>
      <a href="#">FAQS</a>
      <a href="#">LINKING POLICY</a>
      <a href="#">TERMS OF USE</a>
      <a href="#">PRIVACY POLICY</a>
    </nav>
    <p class="copyright">Copyright 2016</p>
  </footer>

</div>
</body>
</html>
```